New Email Signatures for our Employees

Need new Signatures design for our employees, 5 employees in total..we have the logo and some other items we would like on the design.
The Project will include 5 separate email Signatures which will suit all of our employees.
The Project will have a white background and be fresh and inviting.
The project must be in different formats to suit all different applications,which are common in today's emails.
WE are a bathroom retail shop in Australia and it needs to be modern and fresh..if we can start with one signature and if i like it we can do the others.

Target Market(s)

Everyone

Font styles to use
Other font styles liked:
• same as logo

Colors
f37122
1b1b1b

Requirements
Must have
• Our Logo in white background (attached)
• Our Phone number 02 6618 4075
• Our Website www.tidewellbaths.com.au
• Our Address 4/37 Marlow Drive ,Coffs Harbour NSW 2450
• Our Bright Trade Award Logo (attached)
• Our Cartoon of each person for each Signature(attached)
• Email addresses of each employee-
• damon@tidewellbaths.com.au
• Brenda@tidewellbaths.com.au
• Admin@tidewellbaths.com.au
• Tobias@tidewellbaths.com.au
• Rosalind@tidewellbaths.com.au
Nice to have
• not to busy but if we have room-
• "Friends Serving Friends Since 1991"
Should not have
• Should not be too busy
• Should not have other colors other than white,orange and dark grey

```html
<!DOCTYPE html>
<html lang="en">
<head>
<meta charset="UTF-8">
<title>Tidewell Bath – Email Signature</title>
<link href="https://fonts.googleapis.com/css2?family=Mulish:wght@400;600;700&display=swap" rel="stylesheet">
<style>
  :root {
    --orange: #f37122;
    --ink: #1b1b1b;
    --grey: #3d3d3d;
    --mid-grey: #5a5a5a;
    --paper: #ffffff;
    --page: #efefef;
    --skin: #e9c7ae;
    --shirt: #242424;
  }
  * { margin: 0; padding: 0; box-sizing: border-box; }
  html, body {
    width: 1200px; height: 1000px; overflow: hidden;
    background: var(--page);
    font-family: "Mulish", sans-serif;
  }
  .signature {
    position: absolute; left: 20px; top: 54px;
    width: 642px; height: 494px;
    background: var(--paper);
    transform: scale(1.807); transform-origin: top left;
    overflow: hidden;
  }
  .portrait {
    position: absolute; left: 10px; top: 25px; width: 182px; height: 465px;
    border-radius: 60px 60px 8px 8px;
    background: linear-gradient(180deg, var(--skin) 0%, var(--skin) 28%, var(--shirt) 36%, var(--ink) 100%);
  }
  .accent-shape { position: absolute; left: 0; top: 0; width: 642px; height: 494px; }
  .person-name {
    position: absolute; left: 261px; top: 35px;
    font-size: 32px; font-weight: 700; line-height: 1; color: var(--orange);
  }
  .person-role {
    position: absolute; left: 261px; top: 71px;
    font-size: 16px; font-weight: 400; line-height: 1; color: var(--grey);
  }
  .brand-dot {
    position: absolute; left: 346px; top: 122px; width: 66px; height: 66px;
    border-radius: 50%; background: var(--orange);
  }
  .brand-name {
    position: absolute; left: 262px; top: 205px;
    font-size: 24px; font-weight: 400; letter-spacing: 3px; line-height: 1;
    color: var(--mid-grey); text-transform: uppercase; white-space: nowrap;
  }
  .brand-tagline {
    position: absolute; left: 262px; top: 237px;
    font-size: 16px; font-weight: 400; line-height: 1; color: var(--orange); white-space: nowrap;
  }
  .contact {
    position: absolute; left: 268px;
    font-size: 22px; font-weight: 400; line-height: 1; color: var(--grey); white-space: nowrap;
  }
  .contact-phone { top: 323px; }
  .contact-email { top: 359px; }
  .contact-web { top: 396px; left: 270px; }
  .contact-address { top: 436px; line-height: 26px; }
</style>
</head>
<body>
  <main class="signature">
    <div class="portrait" role="img" aria-label="Cartoon of Damon standing in a black company polo shirt and black trousers"></div>

    <svg class="accent-shape" viewBox="0 0 642 494" aria-hidden="true">
      <polygon points="215,50 216,50 219,298 255,313 255,494 215,494" fill="var(--orange)"/>
      <g fill="#fff">
        <path d="M224 329 q11 -8 22 0 l-1 5 h-4 l-1 -3 q-5 -2 -10 0 l-1 3 h-4 z"/>
        <rect x="226" y="335" width="18" height="8" rx="2"/>
      </g>
      <g fill="none" stroke="#fff" stroke-width="1.6">
        <rect x="222" y="363" width="28" height="15" rx="1"/>
        <polyline points="222,363 236,372 250,363"/>
        <line x1="222" y1="378" x2="232" y2="369"/>
        <line x1="250" y1="378" x2="240" y2="369"/>
      </g>
      <g fill="none" stroke="#fff" stroke-width="1.6">
        <circle cx="236" cy="404" r="11"/>
        <ellipse cx="236" cy="404" rx="5" ry="11"/>
        <line x1="225" y1="404" x2="247" y2="404"/>
      </g>
      <path d="M236 462 c-6 -8 -10 -13 -10 -18 a10 10 0 0 1 20 0 c0 5 -4 10 -10 18 z" fill="#fff"/>
      <circle cx="236" cy="444" r="3.5" fill="var(--orange)"/>
    </svg>

    <h1 class="person-name">Damon Halloway</h1>
    <p class="person-role">Business Executive</p>

    <span class="brand-dot" aria-hidden="true"></span>
    <p class="brand-name">Tidewell Bath</p>
    <p class="brand-tagline">Friends Serving Friends Since 1991</p>

    <p class="contact contact-phone">02 6618 4075</p>
    <p class="contact contact-email">damon@tidewellbaths.com.au</p>
    <p class="contact contact-web">www.tidewellbaths.com.au</p>
    <p class="contact contact-address">4/37 Marlow Drive<br>Tarrin Heads NSW 2461</p>
  </main>
</body>
</html>
```